Real Estate Acquisition Company Needs Business Card Design

Tollwyn Real Estate is in need of a business card design!

As a Real Estate Acquisition Company, Tollwyn Real Estate conducts mutually beneficial real estate transactions that actively consider the needs of the seller. At Tollwyn Real Estate we’re actively buying properties from those that see value in a direct transaction, but more importantly want reassurances that they, personally, are in integral part of it. Of course, it all starts with fair market value, but it doesn’t stop there. We’ve found the most success when we offer more. And with our deep experience in this industry, we’ve discovered that we have a lot to offer!

We already have a logo and brand guidelines that we've uploaded. Our final design should stay true to the guidelines. We are looking for a business card design that has two names (Ex. Jane Doe & John Doe) and contact information for each person- this way the company principals can share a card as they often do business as a team.
Updates

The criteria was unfortunately not met on most designs. We are looking for a card that has a layout for TWO names and respective contact information for each of the two people. Almost all designs only had a space for one name and one set of contact information.

Industry/Entity Type

Real Estate

Contact Information for Business Card

We are looking for a business card design that has two names (Ex. Jane Doe & John Doe) and each of their contact information- this way the company principals can share a card as they often do business as a team.

Font styles to use
Other font styles liked:
• Use Brand Guidelines

Requirements
Must have
• Please stay true to our Brand Guidelines for colours, fonts, and positioning of logo.

We require a layout for two names and respective contact information. The company principals work as a team and want a card that has both their information on it.

```html
<!DOCTYPE html>
<html lang="en">
<head>
<meta charset="utf-8">
<title>Tollwyn Real Estate – Business Card</title>
<link rel="stylesheet" href="https://fonts.googleapis.com/css2?family=Ubuntu:wght@400;500;700&display=swap">
<style>
  :root {
    --backdrop: #4a3f37;
    --navy: #1b2638;
    --gold: #f3a935;
    --cream-edge: #f8d592;
    --cream-mid: #fdf1d8;
    --ink: #060606;
    --white: #ffffff;
    --card-w: 880px;
    --card-h: 503px;
  }
  * { box-sizing: border-box; margin: 0; padding: 0; }
  html, body {
    width: 1200px;
    height: 1200px;
    overflow: hidden;
  }
  body {
    background: var(--backdrop);
    font-family: "Ubuntu", sans-serif;
    display: flex;
    flex-direction: column;
    align-items: center;
    justify-content: center;
    gap: 56px;
  }
  .card {
    width: var(--card-w);
    height: var(--card-h);
    position: relative;
    box-shadow: 0 10px 30px rgba(0,0,0,0.35);
  }
  .card-front {
    background: radial-gradient(ellipse at 50% 50%, #ffffff 0%, var(--cream-mid) 45%, var(--cream-edge) 100%);
    display: flex;
    align-items: center;
    justify-content: center;
  }
  .brand {
    display: flex;
    align-items: center;
    gap: 16px;
    font-family: "Ubuntu", sans-serif;
    font-weight: 500;
    letter-spacing: 1px;
    white-space: nowrap;
  }
  .brand-dot {
    border-radius: 50%;
    background: var(--gold);
    flex: none;
  }
  .card-front .brand { color: var(--navy); font-size: 58px; }
  .card-front .brand-dot { width: 34px; height: 34px; }

  .card-back {
    background: var(--ink);
    color: var(--white);
  }
  .card-back .brand {
    position: absolute;
    right: 60px;
    top: 52px;
    color: var(--white);
    font-size: 34px;
    gap: 12px;
  }
  .card-back .brand-dot { width: 20px; height: 20px; }

  .team {
    position: absolute;
    left: 70px;
    right: 60px;
    top: 160px;
    display: grid;
    grid-template-columns: 1fr 1fr;
    column-gap: 40px;
  }
  .person-name {
    font-size: 38px;
    font-weight: 500;
    line-height: 1.1;
  }
  .person-role {
    color: var(--gold);
    font-size: 19px;
    font-weight: 500;
    margin-top: 6px;
  }
  .contact-list {
    list-style: none;
    margin-top: 30px;
    font-size: 19px;
    line-height: 1.25;
  }
  .contact-list li {
    display: flex;
    align-items: flex-start;
    gap: 12px;
    margin-bottom: 9px;
  }
  .contact-list li.address { margin-bottom: 18px; }
  .contact-icon {
    width: 22px;
    height: 22px;
    flex: none;
    margin-top: 1px;
  }
</style>
</head>
<body>

<section class="card card-front" aria-label="Business card front">
  <div class="brand">
    <span class="brand-dot"></span>
    <span class="brand-name">TOLLWYN REAL ESTATE</span>
  </div>
</section>

<section class="card card-back" aria-label="Business card back">
  <div class="brand">
    <span class="brand-dot"></span>
    <span class="brand-name">TOLLWYN REAL ESTATE</span>
  </div>

  <div class="team">
    <article class="person">
      <h1 class="person-name">John Doe</h1>
      <p class="person-role">Director</p>
      <ul class="contact-list">
        <li class="address">
          <svg class="contact-icon" viewBox="0 0 26 26" aria-hidden="true">
            <circle cx="13" cy="13" r="13" fill="var(--gold)"/>
            <path d="M13 6.5a4.5 4.5 0 0 0-4.5 4.5c0 3.3 4.5 8.5 4.5 8.5s4.5-5.2 4.5-8.5A4.5 4.5 0 0 0 13 6.5z" fill="none" stroke="#fff" stroke-width="1.6"/>
            <circle cx="13" cy="11" r="1.6" fill="#fff"/>
          </svg>
          <span>Dummy city,<br>Dummy country, land</span>
        </li>
        <li>
          <svg class="contact-icon" viewBox="0 0 26 26" aria-hidden="true">
            <circle cx="13" cy="13" r="13" fill="var(--gold)"/>
            <path d="M9 7l2.5 0 1.2 3-1.6 1.2a8 8 0 0 0 3.7 3.7l1.2-1.6 3 1.2V17a2 2 0 0 1-2 2A11 11 0 0 1 7 9a2 2 0 0 1 2-2z" fill="#fff"/>
          </svg>
          <span>000.123.1234</span>
        </li>
        <li>
          <svg class="contact-icon" viewBox="0 0 26 26" aria-hidden="true">
            <circle cx="13" cy="13" r="13" fill="var(--gold)"/>
            <g fill="none" stroke="#fff" stroke-width="1.4">
              <circle cx="13" cy="13" r="6"/>
              <ellipse cx="13" cy="13" rx="2.6" ry="6"/>
              <line x1="7" y1="13" x2="19" y2="13"/>
            </g>
          </svg>
          <span>www.tollwynre.com</span>
        </li>
        <li>
          <svg class="contact-icon" viewBox="0 0 26 26" aria-hidden="true">
            <circle cx="13" cy="13" r="13" fill="var(--gold)"/>
            <g fill="none" stroke="#fff" stroke-width="1.4">
              <rect x="7" y="8.5" width="12" height="9" rx="1"/>
              <polyline points="7,9 13,14 19,9"/>
            </g>
          </svg>
          <span>john@tollwynre.com</span>
        </li>
      </ul>
    </article>

    <article class="person">
      <h2 class="person-name">Jane Doe</h2>
      <p class="person-role">Director</p>
      <ul class="contact-list">
        <li class="address">
          <svg class="contact-icon" viewBox="0 0 26 26" aria-hidden="true">
            <circle cx="13" cy="13" r="13" fill="var(--gold)"/>
            <path d="M13 6.5a4.5 4.5 0 0 0-4.5 4.5c0 3.3 4.5 8.5 4.5 8.5s4.5-5.2 4.5-8.5A4.5 4.5 0 0 0 13 6.5z" fill="none" stroke="#fff" stroke-width="1.6"/>
            <circle cx="13" cy="11" r="1.6" fill="#fff"/>
          </svg>
          <span>Dummy city,<br>Dummy country, land</span>
        </li>
        <li>
          <svg class="contact-icon" viewBox="0 0 26 26" aria-hidden="true">
            <circle cx="13" cy="13" r="13" fill="var(--gold)"/>
            <path d="M9 7l2.5 0 1.2 3-1.6 1.2a8 8 0 0 0 3.7 3.7l1.2-1.6 3 1.2V17a2 2 0 0 1-2 2A11 11 0 0 1 7 9a2 2 0 0 1 2-2z" fill="#fff"/>
          </svg>
          <span>000.123.5678</span>
        </li>
        <li>
          <svg class="contact-icon" viewBox="0 0 26 26" aria-hidden="true">
            <circle cx="13" cy="13" r="13" fill="var(--gold)"/>
            <g fill="none" stroke="#fff" stroke-width="1.4">
              <circle cx="13" cy="13" r="6"/>
              <ellipse cx="13" cy="13" rx="2.6" ry="6"/>
              <line x1="7" y1="13" x2="19" y2="13"/>
            </g>
          </svg>
          <span>www.tollwynre.com</span>
        </li>
        <li>
          <svg class="contact-icon" viewBox="0 0 26 26" aria-hidden="true">
            <circle cx="13" cy="13" r="13" fill="var(--gold)"/>
            <g fill="none" stroke="#fff" stroke-width="1.4">
              <rect x="7" y="8.5" width="12" height="9" rx="1"/>
              <polyline points="7,9 13,14 19,9"/>
            </g>
          </svg>
          <span>jane@tollwynre.com</span>
        </li>
      </ul>
    </article>
  </div>
</section>

</body>
</html>
```